Pale Lantern Double Sided Flyer Design

We need a double sided flyer (1/3 of an A4 which is 99mm x 210mm) developed for our Newcastle(NSW) tour. This flyer will be placed in tourist information centres and hotels. We want it to direct people to our website or be able to make bookings over the phone.

About Us:-
We are a city walking tour company that runs tours day or night. We run both day and night and will incorporate real history / real Pale lantern. Some of the stories will be quite serious i.e.- there are infamous murders from 100 years ago, baffling court cases, even a bit of poetry written by murderers, suicides, love triangles, you name it. We will be telling the historical stories that tourists will not hear from any other tour provider. A bit of darkness, a bit of mystery and a bit of history theme.

We do no go for scares and let the very real stories deliver the entertainment for our guests. Our customers enjoy our tours, but it isn't light fun and frivolity. Our stories are being carefully crafted and are packed with unexpected twists, turns; revelations whilst remaining all 100% true. We deliver deep, rich, engaging stories.

Here are a few samples of quotes from the characters in our stories that may give you an idea of the kind of history we will cover:-

"There were bits of spines, bits of skulls, [and] finger bones spilled out all over the streets - I ended up filling three boxes. Children were playing with them for weeks”

"I had a close shave last night and now I want a close haircut.”

“She's a beautiful child', isn't she? She's the cause of all the trouble.”

“I did it because she would not come home with me.”

"I have killed my wife. I’m glad she’s dead.”

"Stand aside or I'll put a bullet through both of you."

“You villain, I'll teach you to take away my character."

“You’re not dead yet, you bastard!”

Our website, booking form and contact details can be viewed at www.palelantern.com.au

Target Market(s)

Tourists

Industry/Entity Type

Tour

Colors

Designer to choose colors to be used in the design.

Requirements
Must have
• Vertical orientation please.
• Please also include a reference to a discount offer of 25% using the promo code "WICK".
Nice to have
• FRONT FLYER INFORMATION
• - Pale Lantern Logo
• - "I have killed my wife; I'm glad she's dead."
• - Harbourside Hidden Lanes Walk
• - 25% Discount Offer Codeword WICK
• - web address at the base; www.palelantern.com.au
• BACK FLYER INFORMATION
• - "She's a beautiful child', isn't she? She's the cause of all the trouble.
• - Pale Lantern Logo at the base along with the web address www.palelantern.com.au
• - Blurb:- Pale lantern brings back Newcastle's hidden past, the forgotten past, the dark past that may not want to be remembered.
• Real stories from the streets around you. Discover the histories you won't hear anywhere else. The forgotten stories of yesteryear finally get a chance to be told. Through you they get to live again.
Should not have
• GENERAL
• Please do not include the phone number, email address or social media icons. We want to drive online bookings.

```html
<!DOCTYPE html>
<html lang="en">
<head>
<meta charset="utf-8">
<title>Pale Lantern Flyer</title>
<link href="https://fonts.googleapis.com/css2?family=Montserrat:wght@300;400;500;600;700;800;900&display=swap" rel="stylesheet">
<style>
:root{
  --red:#e3161f;
  --red-deep:#a80a10;
  --ink:#1d1d1d;
  --dark:#232323;
  --white:#ffffff;
  --stage:#e9e9e9;
  --body:#333333;
}
*{margin:0;padding:0;box-sizing:border-box}
html,body{width:1200px;height:1177px;overflow:hidden;background:var(--stage);font-family:'Montserrat',sans-serif}
.flyer{position:absolute;top:62px;width:490px;height:1040px;background:var(--white);overflow:hidden;box-shadow:0 10px 24px rgba(0,0,0,.18)}
.flyer--front{left:66px}
.flyer--back{left:629px}
.flyer svg.shapes{position:absolute;inset:0}
.brand{position:absolute;left:0;right:0;text-align:center;color:var(--white);font-weight:600;letter-spacing:1px}
.brand--top{top:78px;font-size:22px}
.brand--bottom{top:800px;font-size:30px;line-height:37px}
.brand-dot{display:block;margin:0 auto 14px;width:16px;height:16px;border-radius:50%;background:var(--white)}
.quote{position:absolute;left:0;right:0;text-align:center;color:var(--white)}
.quote--front{top:318px;font-size:35px;font-weight:400;line-height:48px}
.quote--back{top:320px;font-size:19px;font-weight:700;line-height:28px;text-shadow:0 1px 3px rgba(0,0,0,.6)}
.tour-kicker{position:absolute;top:610px;left:0;right:0;text-align:center;color:var(--red);font-size:23px;font-weight:400}
.tour-title{position:absolute;top:638px;left:0;right:0;text-align:center;color:var(--ink);font-size:42px;font-weight:900;letter-spacing:.5px}
.offer{position:absolute;left:20px;top:738px;width:200px;color:var(--white);text-align:center}
.offer-value{font-size:78px;font-weight:900;line-height:80px}
.offer-label{font-size:35px;font-weight:400;line-height:38px}
.offer-word{font-size:35px;font-weight:800;line-height:38px}
.codeword{position:absolute;left:270px;top:782px;color:var(--white);text-align:center;width:170px}
.codeword small{display:block;font-size:14px;font-weight:500}
.codeword strong{font-size:34px;font-weight:900;line-height:36px}
.codeword .mark{position:absolute;top:0;font-size:26px;font-weight:800}
.url{position:absolute;top:934px;left:0;right:0;text-align:center;color:var(--white);font-size:29px;font-weight:800}
.url::before{content:"";display:inline-block;width:16px;height:16px;border-radius:50%;background:var(--red);margin-right:12px;vertical-align:2px}
.book{position:absolute;bottom:0;left:164px;width:162px;height:52px;background:var(--red);border-radius:8px 8px 0 0;color:var(--white);font-size:19px;font-weight:800;text-align:center;line-height:54px}
.welcome{position:absolute;top:470px;left:0;right:0;text-align:center;color:var(--ink);font-size:26px;font-weight:400;line-height:30px}
.welcome-name{position:absolute;top:497px;left:0;right:0;text-align:center;color:var(--red);font-size:37px;font-weight:800;line-height:44px}
.blurb{position:absolute;top:565px;left:19px;width:453px;color:var(--body);font-size:14.6px;font-weight:400;line-height:19.2px;text-align:justify}
.blurb p+p{margin-top:12px}
</style>
</head>
<body>

<section class="flyer flyer--front">
  <svg class="shapes" width="490" height="1040" viewBox="0 0 490 1040">
    <defs>
      <linearGradient id="frontPhoto" x1="0" y1="0" x2="1" y2="1">
        <stop offset="0" stop-color="#3a3a3a"/><stop offset=".6" stop-color="#262626"/><stop offset="1" stop-color="#4a4a4a"/>
      </linearGradient>
    </defs>
    <path role="img" aria-label="Black and white historic photograph of an old stone street building" fill="url(#frontPhoto)" d="M0 128H490V540C400 500 260 510 170 548C100 578 40 575 0 525Z"/>
    <path fill="var(--red)" d="M0 525C40 575 100 578 170 548C260 510 400 500 490 540V556C400 520 260 528 172 566C100 596 38 590 0 548Z"/>
    <rect width="490" height="128" fill="var(--red)"/>
    <circle cx="245" cy="100" r="66" fill="var(--red)"/>
    <rect y="738" width="490" height="144" fill="var(--red)"/>
    <path d="M228 776H490M228 848H490" stroke="var(--red-deep)" stroke-width="3"/>
    <rect x="236" y="780" width="254" height="64" fill="var(--red-deep)" opacity=".55"/>
    <rect y="882" width="490" height="158" fill="var(--dark)"/>
    <circle cx="108" cy="810" r="108" fill="var(--red)"/>
  </svg>
  <div class="brand brand--top">PALE LANTERN</div>
  <p class="quote quote--front">I have killed my wife.<br>I’m glad she’s dead.</p>
  <p class="tour-kicker">HARBOURSIDE HIDDEN</p>
  <h1 class="tour-title">LANES WALK</h1>
  <div class="offer">
    <div class="offer-value">25%</div>
    <div class="offer-label">DISCOUNT</div>
    <div class="offer-word">OFFER</div>
  </div>
  <div class="codeword">
    <span class="mark" style="left:-6px">“</span>
    <small>CODEWORD</small><strong>WICK</strong>
    <span class="mark" style="right:-6px">”</span>
  </div>
  <div class="url">www.palelantern.com.au</div>
  <div class="book">BOOK NOW!</div>
</section>

<section class="flyer flyer--back">
  <svg class="shapes" width="490" height="1040" viewBox="0 0 490 1040">
    <defs>
      <linearGradient id="backPhoto" x1="0" y1="0" x2="0" y2="1">
        <stop offset="0" stop-color="#ffffff"/><stop offset=".22" stop-color="#e6e6e6"/><stop offset=".5" stop-color="#7a7a7a"/><stop offset="1" stop-color="#1e1e1e"/>
      </linearGradient>
    </defs>
    <path role="img" aria-label="Black and white photograph of a city skyline with a cathedral and clock tower above trees" fill="url(#backPhoto)" d="M0 0H490V400C400 372 260 380 170 412C100 440 40 440 0 398Z"/>
    <path fill="var(--red)" d="M0 398C40 440 100 440 170 412C260 380 400 372 490 400V434C400 396 260 398 172 432C100 460 38 456 0 412Z"/>
    <rect x="214" y="547" width="62" height="2" fill="var(--red)"/>
    <rect y="756" width="490" height="138" fill="var(--red)"/>
    <rect y="894" width="490" height="146" fill="var(--dark)"/>
    <circle cx="245" cy="825" r="103" fill="var(--red)"/>
  </svg>
  <p class="quote quote--back">She's a beautiful child', isn't she?<br>She's the cause of all the trouble.</p>
  <p class="welcome">WELCOME TO</p>
  <h2 class="welcome-name">PALE LANTERN</h2>
  <div class="blurb">
    <p>Pale lantern brings back Newcastle's hidden past, the forgotten past, the dark past that may not want to be remembered.</p>
    <p>Real stories from the streets around you. Discover the histories you won't hear anywhere else. The forgotten stories of yesteryear finally get a chance to be told. Through you they get to live again.</p>
  </div>
  <div class="brand brand--bottom"><span class="brand-dot"></span>PALE LANTERN</div>
  <div class="url">www.palelantern.com.au</div>
  <div class="book">BOOK NOW!</div>
</section>

</body>
</html>
```